Design eines privaten Leadership-Leitbildes
Zielgruppe
Es geht um mein privates Leadership-Leitbild. Ich bin CEO eines Unternehmens, das sich in der Schweiz und international intensiv mit der Digitalen Transformation im Bauwesen befasst (www.tlv-bau.ch).
Aufgabenstellung
Die Vorlage ist bereits recht konkret und beinhaltet alles. In der grafischen Aufbereitung ist der Kreative frei. Allerdings geht es um einen Business-Content und bei meinem Leadership-Leitbild um meine persönliche 'Visitenkarte'. Also nicht 'verspielt' oder 'witzig'. Das Plakat soll A4 und A3 genutzt werden und auch auf einem gängigen Laser-Drucker in guter Qualität ausgedruckt werden können.

```html
<!DOCTYPE html>
<html lang="de">
<head>
<meta charset="utf-8">
<title>Leadership-Leitbild – Lukas Brandner</title>
<link href="https://fonts.googleapis.com/css2?family=Bebas+Neue&family=Open+Sans:wght@400;600&display=swap" rel="stylesheet">
<style>
  :root {
    --bg: #4a4a4c;
    --bg-light: #5a5a5c;
    --accent: #d4812d;
    --text: #ffffff;
  }
  html, body { margin: 0; padding: 0; overflow: hidden; }
  body { width: 848px; height: 1200px; background: var(--bg); }
  .poster {
    position: relative;
    width: 848px; height: 1200px;
    background: var(--bg);
    overflow: hidden;
    font-family: "Open Sans", Arial, sans-serif;
    color: var(--text);
  }
  .city-backdrop {
    position: absolute;
    left: 0; top: 230px; width: 848px; height: 970px;
    background:
      radial-gradient(ellipse 40% 45% at 70% 35%, rgba(255,255,255,0.07), transparent 70%),
      radial-gradient(ellipse 60% 30% at 45% 70%, rgba(255,255,255,0.05), transparent 75%);
  }
  .brand {
    position: absolute;
    top: 26px; right: 32px;
    display: flex; align-items: center; gap: 10px;
    font-family: "Open Sans", Arial, sans-serif;
    font-weight: 400; font-size: 13px; letter-spacing: 0.4px;
    color: var(--text);
  }
  .brand-mark { width: 12px; height: 12px; background: var(--text); }
  .title {
    position: absolute; top: 134px; left: 0; width: 848px;
    margin: 0; text-align: center;
    font-family: "Bebas Neue", Impact, sans-serif; font-weight: 400;
    font-size: 66px; line-height: 1; letter-spacing: 0.5px;
  }
  .author {
    position: absolute; top: 209px; left: 0; width: 848px;
    margin: 0; text-align: center;
    font-family: "Bebas Neue", Impact, sans-serif; font-weight: 400;
    font-size: 31px; line-height: 1; letter-spacing: 10px;
    color: var(--accent);
  }
  .section { position: absolute; left: 0; width: 848px; }
  .section-icon { position: absolute; left: 34px; width: 76px; height: 66px; }
  .section-icon svg { width: 100%; height: 100%; stroke: var(--accent); fill: none; stroke-width: 3; }
  .section-body { position: absolute; left: 134px; width: 666px; }
  .kicker {
    margin: 0;
    font-family: "Bebas Neue", Impact, sans-serif; font-weight: 400;
    font-size: 23px; line-height: 1;
  }
  .heading {
    margin: 0;
    font-family: "Bebas Neue", Impact, sans-serif; font-weight: 400;
    font-size: 44px; line-height: 0.95;
    color: var(--accent);
  }
  .copy {
    margin: 2px 0 0;
    font-weight: 600; font-size: 15px; line-height: 17.5px;
    text-transform: uppercase; letter-spacing: -0.1px;
  }
  .copy + .copy { margin-top: 16px; }
</style>
</head>
<body>
<main class="poster">
  <div class="city-backdrop" role="img" aria-label="Stilisierte Stadtsilhouette aus gerasterten Quadraten"></div>

  <div class="brand"><span class="brand-mark"></span><span>TLV · Standards für das Bauwesen</span></div>

  <h1 class="title">Leadership-Leitbild</h1>
  <p class="author">Lukas Brandner</p>

  <section class="section" style="top:322px">
    <div class="section-icon">
      <svg viewBox="0 0 76 66"><ellipse cx="38" cy="33" rx="24" ry="31"/><ellipse cx="38" cy="33" rx="17" ry="24"/><ellipse cx="38" cy="33" rx="10" ry="16"/><line x1="38" y1="24" x2="38" y2="44"/></svg>
    </div>
    <div class="section-body">
      <p class="kicker">Mein</p>
      <h2 class="heading">ID-Statement</h2>
      <p class="copy">Ich bin der klare Laser Richtung Freiheit!</p>
    </div>
  </section>

  <section class="section" style="top:444px">
    <div class="section-icon">
      <svg viewBox="0 0 76 66"><circle cx="28" cy="26" r="22"/><circle cx="28" cy="26" r="14"/><circle cx="28" cy="26" r="6"/><line x1="28" y1="26" x2="70" y2="26"/><polyline points="62,20 70,26 62,32"/><line x1="18" y1="54" x2="38" y2="54"/><line x1="19" y1="60" x2="37" y2="60"/></svg>
    </div>
    <div class="section-body">
      <p class="kicker">Meine</p>
      <h2 class="heading">Mission</h2>
      <p class="copy">Ich fördere Menschen, die mir vertrauen, um gemeinsam Wunder geschehen zu lassen, die uns im Herzen verbinden.</p>
    </div>
  </section>

  <section class="section" style="top:594px">
    <div class="section-icon">
      <svg viewBox="0 0 76 66"><polygon points="14,6 62,6 74,22 38,62 2,22"/><line x1="2" y1="22" x2="74" y2="22"/><polyline points="14,6 26,22 38,6 50,22 62,6"/><polyline points="26,22 38,62 50,22"/></svg>
    </div>
    <div class="section-body">
      <p class="kicker">Meine</p>
      <h2 class="heading">Werte</h2>
      <p class="copy">Authentizität, Integrität, Gestalten, Begeisterung, Verantwortung, Menschlichkeit, Empathie, Klarheit, Transparenz, Weisheit, Weitblick, Erfolg</p>
    </div>
  </section>

  <section class="section" style="top:743px">
    <div class="section-icon">
      <svg viewBox="0 0 76 66"><path d="M2 33 Q38 -6 74 33 Q38 72 2 33 Z"/><circle cx="38" cy="33" r="16"/><circle cx="38" cy="33" r="8"/></svg>
    </div>
    <div class="section-body">
      <p class="kicker">Meine</p>
      <h2 class="heading">Vision</h2>
      <p class="copy">Ich vertraue den Mitarbeitenden und bin offen. Offenheit meint dabei sowohl den offenen Umgang mit Informationen, als auch die Offenheit für Neues und die Freude am Experimentieren.</p>
      <p class="copy">Ich begegne allen Mitarbeitenden auf Augenhöhe. Visionen und Ziele werden gemeinsam entwickelt. Es zählen die besten Argumente und Ideen, keine anderen Faktoren wie Position, Alter, Geschlecht oder Herkunft.</p>
      <p class="copy">Ich begleite und fördere meine Mitarbeitenden. Dazu schaffe ich die notwendigen Räume und Möglichkeiten: Ich gestalte damit den Rahmen und die Struktur für höchste «Performance», und lasse den Mitarbeitenden maximalen Gestaltungsspielraum.</p>
      <p class="copy">Ich fördere und fordere in meiner Organisation Schnelligkeit, Agilität und Flexibilität.</p>
      <p class="copy">Ich sorge dafür, dass uns in allen Aktivitäten stets das weltweit bestmögliche Wissen zur Verfügung steht und baue dafür auf aktiv gelebte Partnerschaften.</p>
    </div>
  </section>
</main>
</body>
</html>
```